Amber Ridge,

Tri-fold brochure. This brochure is designed to get attention from college students who wish to get hands-on broadcast and online experience and do so covering interesting stories and people in places traditional media does not go. I'll be their professor and adviser. Would like the brochure as a single fold using 8.5 X 11 although I would appreciate any suggestions on size or number of folds.

I'm interested in a design the designer is interested in. Love passion. You can see I have this brochure generally mapped out, but I am not stuck on photo placement. I don't care if a photo stretches 2 or 3 pages. I'm interested in other design elements besides my photos and copy.

I've included several photos that can be used. The only photo I'm stuck on is the Marlow Pennick Building for the front page. It's a B&W page completely except for the Chicago flag at the bottom.

```html
<!DOCTYPE html>
<html lang="en">
<head>
<meta charset="utf-8">
<title>Small Town Chicago — Student Media Brochure</title>
<link rel="stylesheet" href="https://fonts.googleapis.com/css2?family=Oxygen:wght@300;400&display=swap">
<style>
  :root {
    --backdrop: #dcdcdc;
    --ink: #1b1b1b;
    --paper-blue: #cdd8e4;
    --tab-blue: #1a8fd2;
    --tab-strip: #8fc0e6;
    --rule: #e6e8ea;
    --cover-black: #161616;
    --white: #ffffff;
    --badge-fill: #f2f6f9;
  }
  * { box-sizing: border-box; margin: 0; padding: 0; }
  html, body {
    width: 1200px; height: 864px; overflow: hidden;
    background: var(--backdrop);
    font-family: "Oxygen", sans-serif;
  }
  .brochure {
    position: absolute; left: 82px; top: 32px;
    width: 1036px; height: 800px;
    display: flex;
    box-shadow: 0 10px 30px rgba(0,0,0,0.18);
  }
  .panel { position: relative; width: 518px; height: 800px; overflow: hidden; }

  /* Inside back panel */
  .panel--inside { background: var(--paper-blue); }
  .mural-photo {
    position: absolute; left: 0; top: 0; width: 518px; height: 318px;
    background:
      linear-gradient(160deg, #3f63a8 0%, #3f63a8 12%, transparent 22%),
      linear-gradient(100deg, #7a3a28 0%, #2a9c8c 35%, #c8874e 55%, #a32a2f 78%, #6e2c22 100%);
  }
  .section { position: absolute; left: 0; width: 518px; }
  .section--positions { top: 320px; height: 275px; }
  .section-rule { position: absolute; left: 0; top: 595px; width: 518px; height: 4px; background: var(--rule); }
  .section--contact { top: 599px; height: 201px; }

  .tab {
    position: absolute; top: 0; bottom: 0; width: 57px;
    background: var(--tab-blue);
    display: flex; align-items: center; justify-content: center;
  }
  .tab::after {
    content: ""; position: absolute; top: 0; bottom: 0; width: 8px;
    background: var(--tab-strip);
  }
  .tab-pointer {
    position: absolute; width: 0; height: 0;
    border-top: 7px solid transparent; border-bottom: 7px solid transparent;
  }
  .section--positions .tab { left: 0; }
  .section--positions .tab::after { right: -8px; }
  .section--positions .tab-pointer { left: 65px; top: 33px; border-left: 12px solid var(--tab-strip); }
  .section--contact .tab { right: 0; }
  .section--contact .tab::after { left: -8px; }
  .section--contact .tab-pointer { right: 65px; top: 28px; border-right: 12px solid var(--tab-strip); }

  .tab-label {
    color: var(--white); font-weight: 300; font-size: 22px;
    letter-spacing: 1px; white-space: nowrap;
  }
  .section--positions .tab-label { transform: rotate(-90deg); }
  .section--contact .tab-label { transform: rotate(90deg); }

  .position-list {
    position: absolute; top: 33px; list-style: none;
    font-size: 11.2px; line-height: 16.6px; color: var(--ink); letter-spacing: 0.3px;
  }
  .position-list li { padding-left: 9px; text-indent: -9px; }
  .position-list li::before { content: "·"; display: inline-block; width: 9px; text-indent: 0; }
  .position-list--a { left: 95px; width: 190px; }
  .position-list--b { left: 300px; width: 200px; }

  .contact-copy {
    position: absolute; top: 26px; right: 107px; width: 345px;
    font-size: 11.2px; line-height: 14.5px; text-align: right; color: var(--ink); letter-spacing: 0.3px;
  }

  /* Front cover panel */
  .panel--cover { background: var(--cover-black); }
  .cover-masthead {
    position: absolute; top: 0; left: 0; width: 518px; height: 138px;
    text-align: right; padding: 22px 21px 0 0; color: var(--white); font-weight: 300;
  }
  .cover-masthead .kicker { display: block; font-size: 40px; line-height: 40px; letter-spacing: 1px; }
  .cover-masthead .title { display: block; font-size: 68px; line-height: 64px; letter-spacing: 0.5px; }
  .cover-photo {
    position: absolute; left: 0; top: 138px; width: 518px; height: 620px;
    border-top: 4px solid var(--white); border-bottom: 4px solid var(--white);
    background:
      linear-gradient(180deg, rgba(235,235,235,0.9) 0%, rgba(160,160,160,0.4) 25%, transparent 45%),
      linear-gradient(90deg, #9a9a9a 0%, #5c5c5c 30%, #474747 50%, #5e5e5e 70%, #8a8a8a 100%);
  }
  .cover-badge {
    position: absolute; left: 24px; top: 656px; width: 130px; height: 84px;
    background: var(--badge-fill);
  }
  .cover-credits {
    position: absolute; right: 21px; top: 652px;
    text-align: right; color: var(--white); font-weight: 300;
    font-size: 22.5px; line-height: 26px; letter-spacing: 0.3px;
  }
</style>
</head>
<body>
<main class="brochure">
  <section class="panel panel--inside">
    <div class="mural-photo" role="img" aria-label="Colourful street mural on a brick building under a blue sky"></div>

    <div class="section section--positions">
      <div class="tab"><span class="tab-label">STUDENT POSITIONS</span></div>
      <span class="tab-pointer"></span>
      <ul class="position-list position-list--a">
        <li>Lorem ipsum dolor rehent qui</li>
        <li>Officipsam quiae</li>
        <li>Dusda si doluptae int et eturion rent et volupti idunt</li>
        <li>Officint et is doluptasimi</li>
        <li>Sitasperest remos di cone sus</li>
        <li>Molor sequibus duciat voluptatis</li>
        <li>Delit eaquis dignit acias alit</li>
        <li>Dolore adi sequae re sum.</li>
      </ul>
      <ul class="position-list position-list--b">
        <li>Lorem ipsum dolor rehent qui</li>
        <li>Officipsam quiae</li>
        <li>Dusda si doluptae int et etur.</li>
        <li>Dion rent et volupti idunt</li>
        <li>Officint et is doluptasimi</li>
        <li>Sitasperest remos di cone sus</li>
        <li>Molor sequibus duciat voluptatis</li>
        <li>Delit eaquis dignit acias alit</li>
        <li>Dolore adi sequae re sum.</li>
      </ul>
    </div>

    <div class="section-rule"></div>

    <div class="section section--contact">
      <p class="contact-copy">Lorem ipsum dolor rehent qui officipsam quiae dusda si doluptae int et etur. Dion rent et volupti idunt officint et is doluptasimi, sitasperest remos di cone sus molor sequibus duciat voluptatis delit eaquis dignit acias alit dolore adi sequae re sum.</p>
      <span class="tab-pointer"></span>
      <div class="tab"><span class="tab-label">CONTACT</span></div>
    </div>
  </section>

  <section class="panel panel--cover">
    <header class="cover-masthead">
      <span class="kicker">SMALL TOWN</span>
      <span class="title">CHICAGO</span>
    </header>
    <div class="cover-photo" role="img" aria-label="Black-and-white upward view of the Marlow Pennick Building against a cloudy sky"></div>
    <div class="cover-badge" role="img" aria-label="City flag"></div>
    <p class="cover-credits">SCHOOL OF COMMUNICATION<br>STUDENT MEDIA CENTER<br>LAKESHORE CREST UNIVERSITY</p>
  </section>
</main>
</body>
</html>
```